Plakat-Design für Verkauf von Bio-zertifiziertem Saatgut
Zielgruppe
Wir sind ein Start Up und verkaufen BIO Zertifiziertes Saatgut für Gemüse, Kräuter, Heilpflanzen und essbare Sprossen etc. Zielgruppe ist vor allem die DIY Community von Jung bis Alt.
Aufgabenstellung
*** INFO*** Da es keine 'Kalender'-Projekte gibt, sollten wir das Projekt unter 'Plakat' einstellen ***INFO***
Wir sind auf der Suche nach einem Design für einen Monatskalender (Deckblatt, 12 Monate, Schlussblatt) der als ewiger Aussaatkalender fungieren soll (Keine Jahreszahlen, nur der Monat). Jeden Monat sollen die Sorten gezeigt werden die jetzt ausgesät werden können. Am Besten teilweise (nicht alle) als Illustrationen oder Bilder. Die Sorten orientieren sich an unserem Saatgutsortiment. Als Unterteilung kann man: 'Vorzucht im Haus', Frühbeet' und 'Direktsaat'
Die Informationen welche Samen wann ausgesät werden, kommen von uns. (Erstmal Platzhalter für das Design nutzen) Falls der Designer Erfahrung in diesem Bereich hat, kann er die Informationen auch selber einfügen. Sonst ist der Designer für Layout und Illustrationen/Bilder zuständig. Toll wäre wenn für jeden Monat noch eine 'Bauernweisheit' zum Thema Pflanzen / Aussaat / Garten hinzugefügt werden kann.
Das Design soll sich an unserer CI der Website www.keimwerk-lutra.de orientieren. Logo, Farben und Fonts (My-Everything, BW Mitga) sind im Anhang beigefügt. Auch die Vorlage der Druckerei ist beigefügt. Format: DIN A4 hoch (210 x 297 mm), beidseitig bedruckt so das man den Kalender auch Aufgeklappt nutzen kann.
Falls noch Informationen benötigt werden, dann meldet euch gerne!

```html
<!DOCTYPE html>
<html lang="de">
<head>
<meta charset="utf-8">
<title>Saatgut Saisonkalender – Keimwerk</title>
<link href="https://fonts.googleapis.com/css2?family=Montserrat:wght@400;500;700;800&family=Allura&display=swap" rel="stylesheet">
<style>
  :root{
    --bg:#b9dde6;
    --cover-dark:#141c22;
    --cover-mid:#1f2d3a;
    --leaf:#2f5a3a;
    --green:#5b7f2a;
    --page:#e8efe5;
    --paper:#ffffff;
    --ink:#3a3a3a;
    --script:#4a4a4a;
    --quote:#5b7a3a;
    --brown:#8a6a3e;
  }
  *{box-sizing:border-box;margin:0;padding:0}
  html,body{width:1200px;height:1200px;overflow:hidden}
  body{background:var(--bg);font-family:"Montserrat",sans-serif;position:relative}

  /* cover */
  .cover{position:absolute;left:50px;top:250px;width:440px;height:630px;
    background:var(--cover-dark);overflow:hidden}
  .cover-photo{position:absolute;inset:0;
    background:radial-gradient(ellipse at 55% 60%,#2e4a2e 0%,#1c2f25 35%,#1a2430 65%,#121820 100%)}
  .cover-photo::after{content:"";position:absolute;left:150px;top:330px;width:160px;height:260px;
    background:linear-gradient(160deg,#c96a2a,#d8823a);opacity:.55;border-radius:40% 40% 10% 10%;filter:blur(18px)}
  .brand-tab{position:absolute;left:145px;top:0;width:145px;height:100px;background:var(--paper);
    border-radius:0 0 12px 12px;display:flex;flex-direction:column;align-items:center;justify-content:center;gap:6px}
  .brand-dot{width:30px;height:30px;border-radius:50%;background:var(--green)}
  .brand-name{font-size:12px;font-weight:500;letter-spacing:2px;color:var(--green)}
  .cover-title{position:absolute;left:0;right:0;top:120px;text-align:center;color:#fff}
  .cover-title h1{font-weight:700;font-size:58px;letter-spacing:2px;line-height:1}
  .cover-title .script{font-family:"Allura",cursive;font-size:54px;font-weight:400;margin-top:-22px;display:block}
  .cover-saying{position:absolute;right:22px;bottom:46px;transform-origin:right bottom;
    transform:rotate(-90deg) translate(100%,0);white-space:nowrap;color:#fff;font-size:9.5px;line-height:1.4;
    position:absolute;right:-2px}
  .cover-saying b{font-weight:700}

  /* month page */
  .month{position:absolute;left:560px;top:210px;width:590px;height:760px;background:var(--page)}
  .binding{position:absolute;top:10px;left:16px;right:16px;display:flex;justify-content:space-between}
  .binding span{width:10px;height:10px;border-radius:50%;background:#cfd6d3}
  .hanger{position:absolute;top:0;left:270px;width:46px;height:18px;background:var(--bg);border-radius:0 0 23px 23px}
  .month-head{text-align:center;padding-top:36px}
  .month-head h2{font-size:46px;font-weight:800;color:var(--green);letter-spacing:1px;line-height:1}
  .month-head .script{font-family:"Allura",cursive;font-size:26px;color:var(--script);display:block;margin-top:-2px}
  .seed-grid{display:grid;grid-template-columns:repeat(3,1fr);row-gap:34px;padding:32px 40px 0}
  .seed{display:flex;flex-direction:column;align-items:center}
  .seed-card{width:84px;height:110px;border-radius:10px;background:linear-gradient(#fff,#fff 55%,rgba(255,255,255,0));
    position:relative;display:flex;justify-content:center}
  .seed-photo{width:76px;height:50px;margin-top:10px;border-radius:22px}
  .seed-name{font-family:"Allura",cursive;font-size:26px;color:var(--script);margin-top:-48px;position:relative}
  .red{background:#c9262a}.sage{background:#7f9a78}.dill{background:#5e9440}.chive{background:#4d7a2e}
  .zucchini{background:#3f6a2c}.jalapeno{background:#2f5a22}.habanero{background:#ef7a1c}.pepper{background:#9ab83a}
  .cherry{background:#b81e22;border-radius:50%;width:58px;height:58px}

  .quote-strip{position:absolute;left:0;right:0;bottom:0;height:96px;background:var(--paper);
    display:flex;align-items:center;padding:0 22px;gap:20px}
  .farmer{width:62px;height:70px;border-radius:8px;background:#e9dcc6;flex:none}
  .quote-strip p{flex:1;text-align:center;color:var(--quote);font-size:13px;letter-spacing:.6px;line-height:1.35}
</style>
</head>
<body>

<section class="cover">
  <div class="cover-photo" role="img" aria-label="Foto: frische Karotten mit Grün in einer Holzkiste auf dunklem Untergrund"></div>
  <div class="brand-tab">
    <span class="brand-dot"></span>
    <span class="brand-name">KEIMWERK</span>
  </div>
  <div class="cover-title">
    <h1>SAATGUT</h1>
    <span class="script">Saisonkalender</span>
  </div>
  <p class="cover-saying"><b>Mit Bauernweißheiten wie diesen:</b><br>Steht das Wasser auf den Äckern, ha'm die Baurn was zu meckern.</p>
</section>

<section class="month">
  <div class="binding">
    <span></span><span></span><span></span><span></span><span></span><span></span><span></span><span></span><span></span><span></span><span></span>
    <span style="visibility:hidden"></span><span style="visibility:hidden"></span>
    <span></span><span></span><span></span><span></span><span></span><span></span><span></span><span></span><span></span><span></span>
  </div>
  <div class="hanger"></div>
  <header class="month-head">
    <h2>JANUAR</h2>
    <span class="script">Saisongemüse</span>
  </header>
  <div class="seed-grid">
    <div class="seed"><div class="seed-card"><div class="seed-photo red" role="img" aria-label="Foto: rote Chilischoten"></div></div><span class="seed-name">Chili</span></div>
    <div class="seed"><div class="seed-card"><div class="seed-photo sage" role="img" aria-label="Foto: Bund Salbei"></div></div><span class="seed-name">Salbei</span></div>
    <div class="seed"><div class="seed-card"><div class="seed-photo cherry" role="img" aria-label="Foto: Cherrychilis"></div></div><span class="seed-name">Cherrychili</span></div>
    <div class="seed"><div class="seed-card"><div class="seed-photo dill" role="img" aria-label="Foto: frischer Dill"></div></div><span class="seed-name">Dill</span></div>
    <div class="seed"><div class="seed-card"><div class="seed-photo sage" role="img" aria-label="Foto: Bund Salbei"></div></div><span class="seed-name">Salbei</span></div>
    <div class="seed"><div class="seed-card"><div class="seed-photo zucchini" role="img" aria-label="Foto: Zucchini"></div></div><span class="seed-name">Zucchini</span></div>
    <div class="seed"><div class="seed-card"><div class="seed-photo red" role="img" aria-label="Foto: rote Chilischoten"></div></div><span class="seed-name">Chili</span></div>
    <div class="seed"><div class="seed-card"><div class="seed-photo jalapeno" role="img" aria-label="Foto: Jalapeños"></div></div><span class="seed-name">Jalapeno</span></div>
    <div class="seed"><div class="seed-card"><div class="seed-photo habanero" role="img" aria-label="Foto: orange Habaneros"></div></div><span class="seed-name">Habanero</span></div>
    <div class="seed"><div class="seed-card"><div class="seed-photo chive" role="img" aria-label="Foto: Bund Schnittlauch"></div></div><span class="seed-name">Schnittlauch</span></div>
    <div class="seed"><div class="seed-card"><div class="seed-photo sage" role="img" aria-label="Foto: Bund Salbei"></div></div><span class="seed-name">Salbei</span></div>
    <div class="seed"><div class="seed-card"><div class="seed-photo pepper" role="img" aria-label="Foto: Zigarrillo-Paprika"></div></div><span class="seed-name">Zigarrelo</span></div>
  </div>
  <footer class="quote-strip">
    <div class="farmer" role="img" aria-label="Illustration: Bauer mit Getreide und Sichel"></div>
    <p>„Entfernen sich die Bienen nicht weit von der Beute,<br>erwarten Schlechtwetter Land und Leute.“</p>
  </footer>
</section>

</body>
</html>
```